Celebration Cake brochure for boutique cake store

Looking for a cake brochure which displays the photo of the cake along with the description. Don't mind what style of brochure or size you do. We are a boutique bakery with both Italian and Australian cakes. I have a few ranges of products that I need to produce brochures (such as other sweets) but this is the first one required. *more photo to come

Industry/Entity Type

Bakery

Font styles to use
Sans Serif

Colors

Designer to choose colors to be used in the design.

Requirements
Must have
• Easy for customers to use the brochure to choose their cake. Don't mind what size brochure/menu you use

```html
<!DOCTYPE html>
<html lang="en">
<head>
<meta charset="utf-8">
<title>Belmonte's Pasticceria – Cakes</title>
<link href="https://fonts.googleapis.com/css2?family=Cinzel:wght@400&family=Oswald:wght@300;400;500&family=Open+Sans:wght@400;600&display=swap" rel="stylesheet">
<style>
:root{
  --ink:#231f20;
  --gold:#b59a4d;
  --red:#b3161f;
  --maroon:#8c1d2f;
  --text:#3a3a3a;
  --rule:#ececec;
  --band:#e6e7e8;
  --cream:#f5f0e3;
  --white:#ffffff;
}
*{margin:0;padding:0;box-sizing:border-box}
html,body{width:830px;height:1200px;overflow:hidden;background:var(--white)}
body{position:relative;font-family:"Open Sans",Arial,sans-serif;color:var(--text)}
.page{position:absolute;left:0;width:830px;height:588px;background:var(--white)}
.page--one{top:0}
.page--two{top:612px}
.divider-band{position:absolute;left:0;top:588px;width:830px;height:24px;background:var(--band)}

/* sidebar */
.sidebar{position:absolute;left:0;top:0;width:113px;height:588px;background:var(--ink);color:var(--white)}
.brand{position:absolute;left:0;top:14px;width:113px;text-align:center}
.brand__mark{display:block;width:60px;height:60px;margin:0 auto 6px;background:var(--maroon)}
.brand__name{font-family:"Cinzel",serif;color:var(--gold);font-size:9px;letter-spacing:1.5px;line-height:1.3}
.pricing{position:absolute;left:10px;top:194px;width:93px}
.pricing__title{font-family:"Cinzel",serif;color:var(--gold);font-size:9.5px;font-weight:400;text-align:center;letter-spacing:.5px}
.pricing__sub{font-size:4.8px;text-align:center;color:#ddd;margin-bottom:8px}
.pricing__rule{border:0;border-top:1px solid #6b6463;margin-bottom:6px}
.price-row{display:flex;justify-content:space-between;align-items:flex-start;height:20px}
.price-row__size{font-family:"Oswald",sans-serif;font-weight:500;font-size:7px;line-height:1}
.price-row__size small{display:block;font-size:4.4px;font-weight:400;color:#ddd;margin-top:1px}
.price-row__amount{font-family:"Oswald",sans-serif;font-size:9.5px;font-weight:300;line-height:1.1}
.price-row__amount sup{font-size:5px}
.gluten{margin-top:10px;padding-top:6px;border-top:1px solid #6b6463;display:flex;justify-content:space-between;font-family:"Oswald",sans-serif;font-weight:500;font-size:6.5px}
.gluten small{font-family:"Open Sans",sans-serif;font-weight:400;font-size:4.5px;color:#ddd}
.gluten-note{font-size:3.9px;font-style:italic;text-align:center;color:#ddd;margin-top:4px;line-height:1.35}
.order__title{position:absolute;left:0;top:432px;width:113px;text-align:center;font-family:"Cinzel",serif;font-weight:400;color:var(--gold);font-size:9px;letter-spacing:.5px}
.order__band{position:absolute;left:0;top:448px;width:113px;height:31px;background:var(--red);text-align:center;padding-top:5px}
.order__cta{font-family:"Oswald",sans-serif;font-weight:400;font-size:10px;line-height:1.1}
.order__web{font-size:5px;letter-spacing:1px;font-weight:600}
.contact{position:absolute;left:10px;top:484px;width:95px;list-style:none;font-size:4.5px;line-height:1.6}
.contact li{display:flex;gap:3px;align-items:flex-start}
.contact svg{flex:none;margin-top:1px}
.contact__note{position:absolute;left:10px;top:537px;width:93px;border-top:1px solid #6b6463;padding-top:5px;font-size:4.1px;text-align:center;line-height:1.4;color:#ddd}
.social{position:absolute;left:0;top:567px;width:113px;display:flex;justify-content:center;gap:4px}
.social span{width:9px;height:9px;border:1px solid #ccc;border-radius:50%}

/* catalogue grid */
.catalogue{position:absolute;left:153px;top:20px;width:637px;display:grid;grid-template-columns:repeat(5,1fr);grid-template-rows:repeat(3,182px)}
.intro{grid-column:1 / span 2;text-align:center;padding-top:64px}
.intro__title{font-family:"Cinzel",serif;font-weight:400;color:var(--gold);font-size:25px;letter-spacing:1px}
.intro__lead{font-size:6.2px;line-height:1.55;color:#555;margin:4px auto 0;width:220px}
.cake{border-left:1px solid var(--rule);text-align:center;padding:16px 7px 0}
.cake--first{border-left:0}
.row-2,.row-3{border-top:1px solid var(--rule)}
.cake__photo{width:92px;height:92px;margin:0 auto 8px;display:flex;align-items:center;justify-content:center}
.cake__photo--dark{background:radial-gradient(circle at 50% 45%,#6b3a1e,#3a1d0e 75%)}
.cake__photo--golden{background:radial-gradient(circle at 50% 50%,#d8a456,#7a4519 78%)}
.cake__photo--cream{background:radial-gradient(circle at 50% 50%,#f0e2b8,#8a5a2b 80%)}
.cake__photo--soon{background:var(--cream);font-family:"Cinzel",serif;font-size:6.3px;color:var(--gold);letter-spacing:.3px}
.cake__name{font-family:"Oswald",sans-serif;font-weight:400;color:var(--red);font-size:8px;line-height:1;letter-spacing:.2px;margin-bottom:3px}
.cake__desc{font-size:5.2px;line-height:1.45;color:#333}
</style>
</head>
<body>

<section class="page page--one">
  <aside class="sidebar">
    <div class="brand"><span class="brand__mark"></span><p class="brand__name">BELMONTE'S<br>PASTICCERIA</p></div>
    <div class="pricing">
      <h3 class="pricing__title">PRICING GUIDE</h3>
      <p class="pricing__sub">prices start from...</p>
      <hr class="pricing__rule">
      <div class="price-row"><p class="price-row__size">8 INCH<small>10 dessert-size slices</small></p><p class="price-row__amount">$38<sup>.00</sup></p></div>
      <div class="price-row"><p class="price-row__size">10 INCH<small>15 dessert-size slices</small></p><p class="price-row__amount">$65<sup>.00</sup></p></div>
      <div class="price-row"><p class="price-row__size">12 INCH<small>20-25 dessert-size slices</small></p><p class="price-row__amount">$80<sup>.00</sup></p></div>
      <div class="price-row"><p class="price-row__size">14 INCH<small>30-35 dessert-size slices</small></p><p class="price-row__amount">$95<sup>.00</sup></p></div>
      <p class="gluten">GLUTEN FREE <small>add $5.00</small></p>
      <p class="gluten-note">Although all care is taken with gluten free/nut free products, they are baked in a kitchen which contains flour &amp; nuts</p>
    </div>
    <h3 class="order__title">ORDER &amp; COLLECT</h3>
    <div class="order__band"><p class="order__cta">Order Cakes Online!</p><p class="order__web">www.belmontecakes.com.au</p></div>
    <ul class="contact">
      <li><svg width="5" height="5" viewBox="0 0 10 10"><path d="M2 1l2 2-1 1.5c.8 1.5 1.8 2.5 3.5 3.5L8 7l2 2-1.5 1C4 9.5.5 6 0 1.5z" fill="#c9a94d"/></svg>07 3100 4821</li>
      <li><svg width="5" height="5" viewBox="0 0 10 10"><path d="M2 1l2 2-1 1.5c.8 1.5 1.8 2.5 3.5 3.5L8 7l2 2-1.5 1C4 9.5.5 6 0 1.5z" fill="#c9a94d"/></svg>07 3100 4822</li>
      <li><svg width="5" height="5" viewBox="0 0 10 10"><rect x="0" y="2" width="10" height="6" fill="#c9a94d"/></svg>orders@belmontecakes.com.au</li>
      <li><svg width="5" height="6" viewBox="0 0 10 12"><path d="M5 0a4 4 0 014 4c0 3-4 8-4 8S1 7 1 4a4 4 0 014-4z" fill="#c9a94d"/></svg>42 Laurel Parade<br>Elmwood, QLD 4099<br>(Market End)</li>
    </ul>
    <p class="contact__note">Collection from Riverside Arcade (Upper Level) available on request only</p>
    <div class="social"><span></span><span></span><span></span></div>
  </aside>

  <div class="catalogue">
    <div class="intro">
      <h2 class="intro__title">CAKES</h2>
      <p class="intro__lead">Lorem ipsum dolor sit amet, consectetur adipiscing elit. Curabitur sed libero elit. Nunc sed egestas urna enean pulvinar magna.</p>
    </div>
    <article class="cake"><div class="cake__photo cake__photo--golden" role="img" aria-label="Apple crumble cake"></div><h4 class="cake__name">APPLE CRUMBLE</h4><p class="cake__desc">Shortbread flan with diced baked apples, cinnamon &amp; a layer of vanilla sponge encased in a crumble topping.</p></article>
    <article class="cake"><div class="cake__photo cake__photo--golden" role="img" aria-label="Apple pie"></div><h4 class="cake__name">APPLE PIE</h4><p class="cake__desc">Baked apple in a tradition short-crust casing.</p></article>
    <article class="cake"><div class="cake__photo cake__photo--dark" role="img" aria-label="Bianco nero profiterole mound"></div><h4 class="cake__name">BIANCO NERO</h4><p class="cake__desc">Italian profiterole mound filled with chantilly cream, smothered in chocolate gianduia cream &amp; decorated with chocolate flakes &amp; strawberries. (Minimum 25 pieces - $3 per profiterole).</p></article>

    <article class="cake cake--first row-2"><div class="cake__photo cake__photo--dark" role="img" aria-label="Black forest cake"></div><h4 class="cake__name">BLACK FOREST</h4><p class="cake__desc">Chocolate sponge soaked with Fioralba liqueur, layers of fresh cream, kirsch sour cherries &amp; finished with fresh cream, chocolate shavings &amp; maraschino cherries.</p></article>
    <article class="cake row-2"><div class="cake__photo cake__photo--cream" role="img" aria-label="Cassata siciliana cake"></div><h4 class="cake__name">CASSATA SICILIAN</h4><p class="cake__desc">Vanilla sponge with Fioralba liqueur, layers of sweet ricotta, glace orange &amp; chocolate bits. Topped with white fondant &amp; glace fruit then wrapped in green marzipan icing.</p></article>
    <article class="cake row-2"><div class="cake__photo cake__photo--dark" role="img" aria-label="Chocolate hazelnut almond mud cake"></div><h4 class="cake__name">CHOCOLATE HAZELNUT<br>ALMOND MUD</h4><p class="cake__desc">Nutty gluten-free cake made with chocolate &amp; almond meal &amp; finished with hazelnut decorations. Gluten free.</p></article>
    <article class="cake row-2"><div class="cake__photo cake__photo--dark" role="img" aria-label="Chocolate mud cake"></div><h4 class="cake__name">CHOCOLATE MUD</h4><p class="cake__desc">Thick melted chocolate sponge with a layer of ganache on top then decorated with chocolate.</p></article>
    <article class="cake row-2"><div class="cake__photo cake__photo--dark" role="img" aria-label="Gluten free chocolate mud cake"></div><h4 class="cake__name">GLUTEN FREE CHOCOLATE MUD</h4><p class="cake__desc">Thick melted chocolate with gluten free sponge and a layer of ganache on top then decorated with chocolate.</p></article>

    <article class="cake cake--first row-3"><div class="cake__photo cake__photo--golden" role="img" aria-label="Croquembouche tower"></div><h4 class="cake__name">CROQUEMBOUSCHE</h4><p class="cake__desc">Profiteroles filled with vanilla &amp; or chocolate crema &amp; topped with toffee – to be served within 2 hours of picking up. (Minimum 25 pieces - $3 per profiterole).</p></article>
    <article class="cake row-3"><div class="cake__photo cake__photo--golden" role="img" aria-label="Crostata di gianduia tart"></div><h4 class="cake__name">CROSTATA DI GIANDUIA</h4><p class="cake__desc">Shortbread tart filled with creamy ganache &amp; Fioralba soaked vanilla sponge surrounded by diced almonds.</p></article>
    <article class="cake row-3"><div class="cake__photo cake__photo--soon">COMING SOON</div><h4 class="cake__name">BAKED CHEESECAKE</h4><p class="cake__desc">Creamy lemon flavoured cheesecake with almonds, fresh cream &amp; fresh strawberries.</p></article>
    <article class="cake row-3"><div class="cake__photo cake__photo--cream" role="img" aria-label="Diplomatica cake"></div><h4 class="cake__name">DIPLOMATICA</h4><p class="cake__desc">Decorated with flakes of pastry &amp; fresh cream, &amp; then dusted with cocoa.</p></article>
    <article class="cake row-3"><div class="cake__photo cake__photo--soon">COMING SOON</div><h4 class="cake__name">FRUIT TART</h4><p class="cake__desc">Shortbread tart with vanilla custard filling &amp; a layer of sponge. Topped with fresh seasonal fruit &amp; glazed with an edge of sliced almonds.</p></article>
  </div>
</section>

<div class="divider-band"></div>

<section class="page page--two">
  <aside class="sidebar">
    <div class="brand"><span class="brand__mark"></span><p class="brand__name">BELMONTE'S<br>PASTICCERIA</p></div>
    <div class="pricing">
      <h3 class="pricing__title">PRICING GUIDE</h3>
      <p class="pricing__sub">prices start from...</p>
      <hr class="pricing__rule">
      <div class="price-row"><p class="price-row__size">8 INCH<small>10 dessert-size slices</small></p><p class="price-row__amount">$38<sup>.00</sup></p></div>
      <div class="price-row"><p class="price-row__size">10 INCH<small>15 dessert-size slices</small></p><p class="price-row__amount">$65<sup>.00</sup></p></div>
      <div class="price-row"><p class="price-row__size">12 INCH<small>20-25 dessert-size slices</small></p><p class="price-row__amount">$80<sup>.00</sup></p></div>
      <div class="price-row"><p class="price-row__size">14 INCH<small>30-35 dessert-size slices</small></p><p class="price-row__amount">$95<sup>.00</sup></p></div>
      <p class="gluten">GLUTEN FREE <small>add $5.00</small></p>
      <p class="gluten-note">Although all care is taken with gluten free/nut free products, they are baked in a kitchen which contains flour &amp; nuts</p>
    </div>
    <h3 class="order__title">ORDER &amp; COLLECT</h3>
    <div class="order__band"><p class="order__cta">Order Cakes Online!</p><p class="order__web">www.belmontecakes.com.au</p></div>
    <ul class="contact">
      <li><svg width="5" height="5" viewBox="0 0 10 10"><path d="M2 1l2 2-1 1.5c.8 1.5 1.8 2.5 3.5 3.5L8 7l2 2-1.5 1C4 9.5.5 6 0 1.5z" fill="#c9a94d"/></svg>07 3100 4821</li>
      <li><svg width="5" height="5" viewBox="0 0 10 10"><path d="M2 1l2 2-1 1.5c.8 1.5 1.8 2.5 3.5 3.5L8 7l2 2-1.5 1C4 9.5.5 6 0 1.5z" fill="#c9a94d"/></svg>07 3100 4822</li>
      <li><svg width="5" height="5" viewBox="0 0 10 10"><rect x="0" y="2" width="10" height="6" fill="#c9a94d"/></svg>orders@belmontecakes.com.au</li>
      <li><svg width="5" height="6" viewBox="0 0 10 12"><path d="M5 0a4 4 0 014 4c0 3-4 8-4 8S1 7 1 4a4 4 0 014-4z" fill="#c9a94d"/></svg>42 Laurel Parade<br>Elmwood, QLD 4099<br>(Market End)</li>
    </ul>
    <p class="contact__note">Collection from Riverside Arcade (Upper Level) available on request only</p>
    <div class="social"><span></span><span></span><span></span></div>
  </aside>

  <div class="catalogue">
    <div class="intro">
      <h2 class="intro__title">CAKES</h2>
      <p class="intro__lead">Lorem ipsum dolor sit amet, consectetur adipiscing elit. Curabitur sed libero elit. Nunc sed egestas urna enean pulvinar magna.</p>
    </div>
    <article class="cake"><div class="cake__photo cake__photo--golden" role="img" aria-label="House special Italian torte"></div><h4 class="cake__name">HOUSE SPECIAL - ITALIAN<br>TORTE</h4><p class="cake__desc">Layers of Fioralba soaked vanilla sponge with chocolate &amp; vanilla custard. Finished with fresh cream rosettes, diced almonds, seasonal fruit &amp; chocolate shards.</p></article>
    <article class="cake"><div class="cake__photo cake__photo--golden" role="img" aria-label="Crostata di ricotta"></div><h4 class="cake__name">CROSTATA DI RICOTTA</h4><p class="cake__desc">Sweet ricotta &amp; chocolate bits inside a shortbread tart glazed with apricot jam &amp; a halo of crushed pistachios.</p></article>
    <article class="cake"><div class="cake__photo cake__photo--soon">COMING SOON</div><h4 class="cake__name">LEMON YOGHURT</h4><p class="cake__desc">Creamy yoghurt baked sponge with fresh lemon &amp; lemon rind, dusted with a sprinkling of icing sugar.</p></article>

    <article class="cake cake--first row-2"><div class="cake__photo cake__photo--cream" role="img" aria-label="Limoncello cake"></div><h4 class="cake__name">LIMONCELLO</h4><p class="cake__desc">Limoncello liqueur flavoured custard between vanilla sponge layers, then covered with sliced lemon, pistachios &amp; sponge crumb.</p></article>
    <article class="cake row-2"><div class="cake__photo cake__photo--golden" role="img" aria-label="Mille foglie cake"></div><h4 class="cake__name">MILLE FOGLIE</h4><p class="cake__desc">Traditional puff pastry vanilla slice made with Italian vanilla custard then topped with pastry flakes &amp; almonds.</p></article>
    <article class="cake row-2"><div class="cake__photo cake__photo--cream" role="img" aria-label="Monte bianco cake"></div><h4 class="cake__name">MONTE BIANCO</h4><p class="cake__desc">Arancio chantilly cream with vanilla sponge surrounded with sponge crumb &amp; topped with a mound of white chocolate.</p></article>
    <article class="cake row-2"><div class="cake__photo cake__photo--dark" role="img" aria-label="Monte nero cake"></div><h4 class="cake__name">MONTE NERO</h4><p class="cake__desc">Arancio chocolate chantilly cream with vanilla sponge surrounded with sponge crumb &amp; topped with a mound of chocolate.</p></article>
    <article class="cake row-2"><div class="cake__photo cake__photo--golden" role="img" aria-label="Nocciola cake"></div><h4 class="cake__name">NOCCIOLA</h4><p class="cake__desc">Hazelnut flavoured cream with vanilla &amp; Fioralba liqueur covered in almonds &amp; strawberries.</p></article>

    <article class="cake cake--first row-3"><div class="cake__photo cake__photo--golden" role="img" aria-label="Orange almond cake"></div><h4 class="cake__name">ORANGE ALMOND</h4><p class="cake__desc">Fresh oranges sliced onto an almond meal &amp; orange flavoured cake then topped with glaze &amp; surrounded with diced almonds &amp; soft icing. Gluten free.</p></article>
    <article class="cake row-3"><div class="cake__photo cake__photo--soon">COMING SOON</div><h4 class="cake__name">VANILLA, STRAWBERRIES &amp;<br>CREAM</h4><p class="cake__desc">Home style vanilla sponge with a layer of raspberry jam, fresh cream, chopped strawberries, dusted with icing sugar.</p></article>
    <article class="cake row-3"><div class="cake__photo cake__photo--dark" role="img" aria-label="Tartufo bacio cake"></div><h4 class="cake__name">TARTUFO BACIO</h4><p class="cake__desc">Hazelnut meringue base, topped with layers of chocolate sponge soaked with Fioralba, gianduia cream then surrounded in pistachios - the top is then decorated with a carnation of chocolate fans.</p></article>
    <article class="cake row-3"><div class="cake__photo cake__photo--cream" role="img" aria-label="Tiramisu cake"></div><h4 class="cake__name">TIRAMISU</h4><p class="cake__desc">Italian 'pick-me-up' torte consisting of savoiardi dipped in coffee liqueur between layers of mascarpone cream then covered in white chocolate shards all over.</p></article>
    <article class="cake row-3"><div class="cake__photo cake__photo--soon">COMING SOON</div><h4 class="cake__name">PEAR &amp; ALMOND</h4><p class="cake__desc">An almond and pear baked teacake, glazed and decorated with desiccated coconut.</p></article>
  </div>
</section>

</body>
</html>
```